Heavy Equipment Service Technician

K&T Equipment Corp. is a family owned industry leader that’s been supplying construction equipment, tractors and landscaping gear to Southern Connecticut for the past 81 years. Located on Route 9 in Orange, we help home builders, site excavators, road builders, municipalities, landscapers, home owners and many more. We believe we can make work fun and easy by supplying new and used equipment, equipment rentals, service, parts and advice. Our fast paced service department is ready to expand! We are looking for a Heavy Equipment Service Technician, Experience Required.

QUALIFICATIONS AND SKILL:

· Must have a valid driver’s license.

· Must be reliable, hard working and have a professional work ethic.

· Must own tools and have the ability to work independently.

· Must have the ability to lift, push, pull 70+ pounds, climb heavy. equipment safely, bend and kneel.

· Must be able to perform basic equipment service: ie: filters, oils, inspections.

· Must possess a willingness to learn and grow.

· Must provide own tools.

RESPONSIBILITIES AND DUTIES:

· Perform scheduled services on heavy equipment and tractors.

· Perform final assembly of tractors.

· Perform body work on equipment.

· Perform minor welding on equipment and tractors.

· Keep work space clean of all debris.

Hi, This, is my first time using Mint Lantern! I am looking to design a new web page on our website that I can direct prospective employees. This webpage I want to look very professional to attract new employees. I am hoping to show off the wonderful benefits we offer, the fun work place and a great place to grow.

```html
<!DOCTYPE html>
<html lang="en">
<head>
<meta charset="utf-8">
<title>Heavy Equipment Service Technician – K&amp;T Equipment Corp.</title>
<link href="https://fonts.googleapis.com/css2?family=Outfit:wght@300;400;500;600;700;800&display=swap" rel="stylesheet">
<style>
  :root {
    --yellow: #ffd200;
    --yellow-footer: #efc40a;
    --yellow-bar: #f2c80c;
    --yellow-soft: #fff8dc;
    --ink: #151515;
    --navy: #0e1b2e;
    --text: #2a2a2a;
    --field: #eeeeee;
    --line: #d9d9d9;
    --panel: #f4f4f6;
    --white: #ffffff;
  }
  * { margin: 0; padding: 0; box-sizing: border-box; }
  html, body { width: 1200px; height: 3488px; overflow: hidden; }
  body { position: relative; background: var(--white); font-family: "Outfit", sans-serif; color: var(--text); }
  .abs { position: absolute; }

  /* Hero */
  .hero-photo { position: absolute; left: 0; top: 0; width: 1200px; height: 770px; }
  .hero-lines { position: absolute; left: 0; top: 0; width: 1200px; height: 860px; }
  .brand-box { left: 125px; top: 0; width: 82px; height: 106px; background: var(--white); display: flex; align-items: center; justify-content: center; flex-direction: column; gap: 6px; }
  .brand-box .dot { width: 26px; height: 26px; border-radius: 50%; background: var(--yellow); }
  .brand-box .name { font-size: 12px; font-weight: 700; color: var(--ink); text-align: center; line-height: 1.05; }
  .nav a { position: absolute; top: 24px; color: var(--white); font-size: 19px; text-decoration: none; font-weight: 400; }
  .phone-pill { left: 926px; top: 19px; width: 142px; height: 33px; border-radius: 17px; background: var(--yellow); color: var(--white); font-size: 13px; font-weight: 600; display: flex; align-items: center; justify-content: center; gap: 6px; }
  .hero-title { left: 167px; top: 262px; font-size: 96px; font-weight: 700; color: var(--white); line-height: 1; letter-spacing: -1px; }
  .hero-sub { left: 167px; top: 374px; font-size: 24px; color: var(--white); font-weight: 400; }
  .apply-btn { left: 171px; top: 436px; width: 128px; height: 36px; border-radius: 18px; background: var(--yellow); color: var(--white); font-size: 15px; font-weight: 600; display: flex; align-items: center; justify-content: center; }

  .contact-shadow { left: 789px; top: 451px; width: 279px; height: 401px; background: var(--yellow); }
  .contact-card { left: 771px; top: 431px; width: 278px; height: 402px; background: var(--white); box-shadow: 0 4px 18px rgba(0,0,0,0.08); padding: 22px 24px; }
  .contact-card h3 { font-size: 24px; font-weight: 500; color: var(--ink); margin-bottom: 15px; }
  .field { width: 234px; height: 30px; background: var(--field); font-size: 11px; color: #555; padding: 0 12px; display: flex; align-items: center; justify-content: space-between; margin-bottom: 14px; }
  .field.message { height: 93px; align-items: flex-start; padding-top: 10px; }
  .send-btn { width: 105px; height: 34px; background: var(--yellow); color: var(--white); font-size: 15px; font-weight: 600; display: flex; align-items: center; justify-content: center; margin-top: -2px; }

  /* Intro */
  .intro-title { left: 130px; top: 945px; font-size: 49px; line-height: 58px; color: var(--ink); font-weight: 400; }
  .intro-title strong { font-weight: 800; }
  .intro-rule { left: 479px; top: 945px; width: 2px; height: 228px; background: var(--yellow); }
  .intro-text { left: 542px; top: 990px; width: 525px; font-size: 14.5px; line-height: 27.5px; color: #333; }

  /* Services ring */
  .service-band { position: absolute; left: 0; top: 1470px; width: 1200px; height: 480px; }
  .ring { left: 370px; top: 1322px; width: 460px; height: 460px; border-radius: 50%; border: 1px solid var(--line); }
  .ring-dot { width: 14px; height: 14px; border-radius: 50%; background: var(--yellow); }
  .ring-brand { left: 430px; top: 1430px; width: 340px; height: 240px; display: flex; flex-direction: column; align-items: center; justify-content: center; gap: 16px; }
  .ring-brand .disc { width: 110px; height: 110px; border-radius: 50%; background: var(--yellow); }
  .ring-brand .name { font-size: 40px; font-weight: 800; color: var(--ink); }
  .ring-label { font-size: 17px; font-weight: 600; color: #2b2b2b; line-height: 24px; }

  /* Lists */
  .section-heading { font-size: 31px; font-weight: 700; color: var(--navy); letter-spacing: -0.3px; }
  .check-list { list-style: none; }
  .check-list li { position: absolute; font-size: 18px; line-height: 23px; color: var(--navy); padding-left: 27px; }
  .check-list li::before { content: ""; position: absolute; left: 0; top: 3px; width: 16px; height: 16px; border-radius: 50%; background: var(--yellow); box-shadow: inset 0 0 0 4px #f7f7f7; border: 1px solid #e2b800; }
  .photo-shadow { background: var(--yellow); }
  .photo { box-shadow: 0 4px 10px rgba(0,0,0,0.15); }

  .duties-panel { left: 3px; top: 2596px; width: 1197px; height: 556px; background: linear-gradient(90deg, #f7f7f9 0%, #eeeef2 55%, #f6f6f8 100%); }

  /* Footer */
  .footer { left: 0; top: 3152px; width: 1200px; height: 274px; background: var(--yellow-footer); }
  .footer-bar { left: 0; top: 3426px; width: 1200px; height: 62px; background: var(--yellow-bar); font-size: 11px; color: var(--ink); }
  .f-col { position: absolute; top: 3228px; }
  .f-col .mark { width: 30px; height: 2px; background: var(--white); margin-bottom: 14px; }
  .f-col h4 { font-size: 16px; font-weight: 400; color: var(--ink); margin-bottom: 16px; }
  .f-col a { display: block; font-size: 11.5px; color: var(--ink); text-decoration: none; line-height: 22px; }
  .f-divider { top: 3212px; width: 1px; height: 200px; background: rgba(0,0,0,0.15); }
  .f-contact { display: flex; align-items: center; gap: 9px; font-size: 11.5px; color: var(--ink); height: 34px; }
  .news-input { width: 119px; height: 27px; background: var(--white); font-size: 9px; color: #999; padding-left: 10px; display: flex; align-items: center; }
  .news-btn { width: 27px; height: 27px; background: var(--yellow); display: flex; align-items: center; justify-content: center; }
  .social { width: 24px; height: 24px; border-radius: 50%; background: var(--ink); }
</style>
</head>
<body>

<!-- Hero -->
<svg class="hero-photo" viewBox="0 0 1200 770" role="img" aria-label="Photo of a technician in navy coveralls seated in front of a yellow heavy equipment machine">
  <defs>
    <linearGradient id="heroTone" x1="0" y1="0" x2="1" y2="1">
      <stop offset="0" stop-color="#6b5312"/>
      <stop offset="0.45" stop-color="#3a3022"/>
      <stop offset="1" stop-color="#a88a1c"/>
    </linearGradient>
  </defs>
  <polygon points="0,0 1200,0 1200,332 433,769 0,519" fill="url(#heroTone)"/>
</svg>
<svg class="hero-lines" viewBox="0 0 1200 860">
  <g stroke="#bdbdbd" stroke-width="1" fill="none">
    <line x1="43" y1="694" x2="170" y2="623"/>
    <line x1="135" y1="664" x2="217" y2="623"/>
    <line x1="392" y1="830" x2="772" y2="615"/>
    <line x1="580" y1="830" x2="772" y2="718"/>
    <line x1="1068" y1="467" x2="1200" y2="396"/>
  </g>
</svg>

<div class="abs brand-box"><span class="dot"></span><span class="name">K&amp;T<br>Equipment</span></div>
<nav class="nav">
  <a href="#" style="left:663px">Home</a>
  <a href="#" style="left:758px">Contact Us</a>
</nav>
<div class="abs phone-pill">
  <svg width="12" height="12" viewBox="0 0 24 24" fill="#fff"><path d="M6.6 10.8a15.1 15.1 0 0 0 6.6 6.6l2.2-2.2a1 1 0 0 1 1-.25 11.4 11.4 0 0 0 3.6.57 1 1 0 0 1 1 1V20a1 1 0 0 1-1 1A17 17 0 0 1 3 4a1 1 0 0 1 1-1h3.5a1 1 0 0 1 1 1c0 1.25.2 2.45.57 3.57a1 1 0 0 1-.25 1z"/></svg>
  203-555-0147
</div>

<h1 class="abs hero-title">We Hire</h1>
<p class="abs hero-sub">Heavy Equipment Service Technician</p>
<div class="abs apply-btn">Apply Now</div>

<div class="abs contact-shadow"></div>
<form class="abs contact-card">
  <h3>Contact Us</h3>
  <div class="field">Name</div>
  <div class="field">Email</div>
  <div class="field">Phone <svg width="8" height="5" viewBox="0 0 8 5"><polygon points="0,0 8,0 4,5" fill="#555"/></svg></div>
  <div class="field message">Message</div>
  <div class="send-btn">Send Us</div>
</form>

<!-- Intro -->
<h2 class="abs intro-title">HEAVY<br>EQUIPMENT<br><strong>SERVICE<br>TECHNICIAN</strong></h2>
<div class="abs intro-rule"></div>
<p class="abs intro-text">Lorem Ipsum is simply dummy text of the printing and typesetting industry. Lorem Ipsum has been the industry's standard dummy text ever since the 1500s, when an unknown printer took a galley of type and scrambled it to make a type specimen book. It has survived not only five centuries,</p>

<!-- Services ring -->
<svg class="service-band" viewBox="0 0 1200 480">
  <polygon points="0,12 1200,115 1200,290 535,466 0,130" fill="var(--yellow-soft)"/>
</svg>
<div class="abs ring"></div>
<div class="abs ring-dot" style="left:421px;top:1389px"></div>
<div class="abs ring-dot" style="left:763px;top:1389px"></div>
<div class="abs ring-dot" style="left:421px;top:1696px"></div>
<div class="abs ring-dot" style="left:763px;top:1696px"></div>
<div class="abs ring-brand"><span class="disc"></span><span class="name">K&amp;T Equipment</span></div>
<div class="abs ring-label" style="left:214px;top:1370px;width:160px;text-align:right">Supplying New &amp;<br>Used Equipment</div>
<div class="abs ring-label" style="left:810px;top:1378px">Equipment Rentals</div>
<div class="abs ring-label" style="left:280px;top:1691px;width:100px;text-align:right">Service</div>
<div class="abs ring-label" style="left:810px;top:1691px">Parts &amp; Advice</div>

<!-- Qualifications -->
<h2 class="abs section-heading" style="left:130px;top:2011px">QUALIFICATIONS AND SKILL</h2>
<ul class="check-list">
  <li style="left:142px;top:2108px;width:380px">Must have a valid driver’s license.</li>
  <li style="left:142px;top:2149px;width:360px">Must be reliable, hard working and have a professional work ethic.</li>
  <li style="left:142px;top:2203px;width:360px">Must own tools and have the ability to work independently.</li>
  <li style="left:142px;top:2257px;width:380px">Must have the ability to lift, push, pull 70+ pounds, climb heavy. equipment safely, bend and kneel.</li>
  <li style="left:142px;top:2340px;width:360px">Must be able to perform basic equipment service: ie: filters, oils, inspections.</li>
  <li style="left:142px;top:2401px;width:400px">Must possess a willingness to learn and grow.</li>
  <li style="left:142px;top:2439px;width:380px">Must provide own tools.</li>
</ul>
<div class="abs photo-shadow" style="left:611px;top:2118px;width:475px;height:367px"></div>
<div class="abs photo" role="img" aria-label="Photo of a mechanic in an orange hard hat and shirt working beneath heavy machinery" style="left:593px;top:2100px;width:475px;height:367px;background:linear-gradient(135deg,#4a3a2c 0%,#8a5a34 35%,#e2562a 60%,#3b3a38 100%)"></div>

<!-- Responsibilities -->
<div class="abs duties-panel"></div>
<div class="abs photo" role="img" aria-label="Photo of a gloved hand holding a wrench next to a thumbs-up hand" style="left:130px;top:2684px;width:475px;height:367px;background:linear-gradient(120deg,#2c3d4c 0%,#6d7580 40%,#b58a72 65%,#8aa0b0 100%)"></div>
<h2 class="abs section-heading" style="left:686px;top:2692px;font-size:25px">RESPONSIBILITIES AND DUTIES</h2>
<ul class="check-list">
  <li style="left:700px;top:2765px;width:320px">Perform scheduled services on heavy equipment and tractors.</li>
  <li style="left:700px;top:2839px;width:340px">Perform final assembly of tractors.</li>
  <li style="left:700px;top:2890px;width:340px">Perform body work on equipment.</li>
  <li style="left:700px;top:2942px;width:320px">Perform minor welding on equipment and tractors.</li>
  <li style="left:700px;top:3015px;width:340px">Keep work space clean of all debris.</li>
</ul>

<!-- Footer -->
<footer>
  <div class="abs footer"></div>
  <div class="abs f-divider" style="left:287px"></div>
  <div class="abs f-divider" style="left:527px"></div>
  <div class="abs f-divider" style="left:849px"></div>

  <div class="f-col" style="left:162px">
    <div class="mark"></div>
    <h4>Site Links</h4>
    <a href="#">K&amp;T Equipment</a>
    <a href="#">Sales, Service &amp; Rentals</a>
    <a href="#">HOME</a>
    <a href="#">NEW EQUIPMENT</a>
    <a href="#">GENERATORS</a>
    <a href="#">USED EQUIPMENT</a>
  </div>
  <div class="f-col" style="left:343px">
    <div class="mark"></div>
    <h4>Site Links</h4>
    <a href="#">RENTALS</a>
    <a href="#">PARTS</a>
    <a href="#">SERVICE</a>
    <a href="#">SALES</a>
    <a href="#">ABOUT US</a>
    <a href="#">CONTACT US</a>
  </div>
  <div class="f-col" style="left:575px">
    <div class="mark"></div>
    <h4>Contact Us</h4>
    <div class="f-contact">
      <svg width="14" height="14" viewBox="0 0 24 24" fill="none" stroke="#151515" stroke-width="1.6"><path d="M6.6 10.8a15.1 15.1 0 0 0 6.6 6.6l2.2-2.2a1 1 0 0 1 1-.25 11.4 11.4 0 0 0 3.6.57 1 1 0 0 1 1 1V20a1 1 0 0 1-1 1A17 17 0 0 1 3 4a1 1 0 0 1 1-1h3.5a1 1 0 0 1 1 1c0 1.25.2 2.45.57 3.57a1 1 0 0 1-.25 1z"/></svg>
      Phone: 415-555-0192
    </div>
    <div class="f-contact">
      <svg width="14" height="14" viewBox="0 0 24 24" fill="none" stroke="#151515" stroke-width="1.6"><path d="M12 22s7-7 7-12a7 7 0 0 0-14 0c0 5 7 12 7 12z"/><circle cx="12" cy="10" r="2.5"/></svg>
      Address, City
    </div>
    <div class="f-contact">
      <svg width="14" height="14" viewBox="0 0 24 24" fill="none" stroke="#151515" stroke-width="1.6"><rect x="3" y="5" width="18" height="14" rx="1"/><path d="M3 6l9 7 9-7"/></svg>
      info@ktequipcorp.com
    </div>
  </div>
  <div class="f-col" style="left:891px">
    <div class="mark"></div>
    <h4>Newsletter</h4>
    <div style="display:flex">
      <div class="news-input">Email..</div>
      <div class="news-btn"><svg width="12" height="12" viewBox="0 0 24 24" fill="#fff"><path d="M2 11l20-9-9 20-2-9z"/></svg></div>
    </div>
    <div style="display:flex;gap:6px;margin-top:25px">
      <span class="social"></span><span class="social"></span><span class="social"></span>
    </div>
  </div>

  <div class="abs footer-bar">
    <span class="abs" style="left:202px;top:23px">@2022 Ktequip | All Rights Reserved.</span>
    <span class="abs" style="left:811px;top:23px">Terms &amp; Conditions &nbsp;|&nbsp; Privacy Policy</span>
  </div>
</footer>

</body>
</html>
```